Stationery Design

Need a stationery design for an established accounting firm based in London, England.

The company’s name is ‘Marcus Fenwell’. We provide a broad range of bookkeeping, accounting, audit, tax and business services to a wide range of clients (ie, individuals, company, partnerships, etc).

The stationary design needs to show strength and trust and should be clean, corporate and professional.

Only 2 colours must be used as noted on the logo.

The fonts are in Optima

We need the following:

#1: Business Cards (design on 2 sides)
#2: Letterhead (word format) and can be sent to printers
#3: Continuation sheets (word format) and can be sent to printers
#4: Sales invoice template (word format) and can be sent to printers
#5: Report Cover front and back for binding,
#6: Complimentary Slips,
#7: Legal corners with our logo only
#7: Email signature templates

I have attached my company's logo in various file formats

We also need to have our accountancy association’s logo and this must be in the same colour as the dark blue. This BRTQ logo must be at least 8mm square (can be larger). I have attached the BRTQ logo in various file formats

I have also attached other information that you will need for the letter head and invoice templates

I have also attached our old letterhead, fee note template for reference
Updates

Dear Designers - I have increased the budget

Dear Designers - I have read your comments on the fact that the prize does not reflect the work. Thank you and I appreciate your comments. Unfortunately, I am a start up and my budget is limited. As an Alternative, I have reduced the work that I am asking for to the following items and I hope you can assist: #1: Business Cards (design on 2 sides) #2: Letterhead (word format) and can be sent to printers #3: Report Cover front and back for binding, #4: Email signature templates Regards

Reason: I have reduced the work to be done and hence want to capture more designers.

Industry/Entity Type

Accounting

```html
<!DOCTYPE html>
<html lang="en">
<head>
<meta charset="utf-8">
<title>Marcus Fenwell – Stationery</title>
<link rel="stylesheet" href="https://fonts.googleapis.com/css2?family=Marcellus&family=Crimson+Text:wght@400;600&display=swap">
<style>
  :root {
    --navy: #1d3f6e;
    --plum: #8b2a7f;
    --paper: #ffffff;
    --backdrop: #ececec;
    --ink: #222a36;
    --edge: #d6d6d6;
  }
  * { box-sizing: border-box; margin: 0; padding: 0; }
  html, body { width: 1200px; height: 880px; overflow: hidden; }
  body {
    background: var(--backdrop);
    font-family: "Crimson Text", Georgia, serif;
    color: var(--ink);
    position: relative;
  }
  address { font-style: normal; }
  .sheet, .card {
    position: absolute;
    background: var(--paper);
    border: 1px solid var(--edge);
    box-shadow: 0 4px 14px rgba(0,0,0,0.08);
  }
  .brand {
    display: flex;
    align-items: center;
    gap: 10px;
  }
  .brand-square {
    display: block;
    background: var(--navy);
    flex: none;
  }
  .brand-name {
    font-family: "Marcellus", "Optima", sans-serif;
    color: var(--navy);
    letter-spacing: 0.02em;
    white-space: nowrap;
  }

  /* Letterhead */
  .letterhead { left: 40px; top: 30px; width: 580px; height: 820px; }
  .letterhead .brand { position: absolute; left: 44px; top: 44px; }
  .letterhead .brand-square { width: 30px; height: 30px; }
  .letterhead .brand-name { font-size: 27px; }
  .letterhead-footer {
    position: absolute; left: 40px; right: 40px; bottom: 34px;
    text-align: center;
    font-size: 9.5px; line-height: 1.4; color: var(--ink);
  }
  .association-badge {
    display: block; width: 58px; height: 58px;
    margin: 0 auto 10px; background: var(--navy);
  }
  .letterhead-footer .emph { font-weight: 600; }

  /* Business cards */
  .card-back { left: 670px; top: 70px; width: 470px; height: 300px; }
  .card-back .brand { position: absolute; left: 50%; top: 50%; transform: translate(-50%, -50%); gap: 14px; }
  .card-back .brand-square { width: 40px; height: 40px; }
  .card-back .brand-name { font-size: 36px; }

  .card-front { left: 670px; top: 470px; width: 470px; height: 300px; }
  .card-front .brand { position: absolute; left: 26px; top: 28px; gap: 7px; }
  .card-front .brand-square { width: 18px; height: 18px; }
  .card-front .brand-name { font-size: 17px; }
  .card-person {
    position: absolute; left: 0; right: 0; top: 92px; text-align: center;
  }
  .person-name {
    font-family: "Marcellus", "Optima", sans-serif;
    font-size: 34px; color: var(--navy); letter-spacing: 0.03em; font-weight: 400;
  }
  .person-role {
    font-family: "Marcellus", "Optima", sans-serif;
    font-size: 22px; color: var(--plum); margin-top: 2px;
  }
  .card-contact {
    position: absolute; right: 26px; top: 28px;
    text-align: right; font-size: 11px; line-height: 1.4; color: var(--navy);
  }
  .card-address {
    position: absolute; left: 26px; bottom: 26px;
    font-size: 11px; line-height: 1.4; color: var(--navy);
  }
</style>
</head>
<body>

  <section class="sheet letterhead" aria-label="Letterhead">
    <div class="brand">
      <span class="brand-square"></span>
      <span class="brand-name">MARCUS FENWELL</span>
    </div>
    <footer class="letterhead-footer">
      <span class="association-badge" aria-hidden="true"></span>
      <p>12 Aldwin House, Calloway Business Park, Thornbury Road, Ellerby Cross, Westmarsh, WM4 7QP</p>
      <p>Tel: 020 7946 0321 &nbsp; www.marcusfenwell.co.uk</p>
      <p class="emph">Company Registered in England and Wales No: 08527741</p>
      <p class="emph">Registered as auditors and regulated for a range of business activities in the United Kingdom by the</p>
      <p class="emph">Board of Registered Tax Qualifiers</p>
    </footer>
  </section>

  <section class="card card-back" aria-label="Business card, reverse">
    <div class="brand">
      <span class="brand-square"></span>
      <span class="brand-name">MARCUS FENWELL</span>
    </div>
  </section>

  <section class="card card-front" aria-label="Business card, front">
    <div class="brand">
      <span class="brand-square"></span>
      <span class="brand-name">MARCUS FENWELL</span>
    </div>
    <address class="card-contact">
      Tel: 020 7946 0321<br>
      mail@marcusfenwell.co.uk
    </address>
    <div class="card-person">
      <h1 class="person-name">JOHN DOE</h1>
      <p class="person-role">Manager</p>
    </div>
    <address class="card-address">
      12 Aldwin House<br>
      Calloway Business Park<br>
      Thornbury Road<br>
      Ellerby Cross<br>
      Westmarsh, WM4 7QP
    </address>
  </section>

</body>
</html>
```